Business Cards for a company that provides webstore services to veterinarians

We need business cards designed for our main service PawCartHub. PawCartHub is a webstore that veterinarian clinics can use to that will allow their clients to purchase products for their pets. Our company is Brindlow Veterinary Solutions (BVS). Our mission statement is We love pets! We will do everything possible to facilitate along, healthy and happy relationship with their families.

Target Market(s)

Veterinarians

Industry/Entity Type

Veterinary

Contact Information for Business Card

I would like the design to incorporate the colours our our company. Cards should have room for employee name, title (only necessary in two instances), phone number, mobile number, email address and linkedin symbol and related profile name ie Marla Quinton. I would like the PawCartHub logo to appear on one side and BVS logo to appear on the other. I will need both an english and french version. I can provide the french translation. Please focus on english version and then we will translate

Colors

Designer to choose colors to be used in the design.

Requirements
Must have
• one side - PawCartHub logo with persons name, phone number, mobile number, email address
• second side - BVS logo
• colours should be consistent with our company. colours are as follows:
• Red
• RGB: 190 / 30 / 45
• CYMK: 14 / 100 / 90 /10
• Hex: #BE1E2D
• Gray
• RGB: 88 / 89 / 86
• CYMK: 3 / 2 / 0 /64
• Hex: #585956
Nice to have
• address of company - can be on either side address is 4817 Feldmoor Street Suite 305 Burlington ON K2R 6T4. Toll free number will vary depending on person
• Linkedin symbol and name of person
• on second side with BVS logo our company's mission statement
Should not have
• nothing comes to mind

```html
<!DOCTYPE html>
<html lang="en">
<head>
<meta charset="utf-8">
<title>PawCartHub Business Card</title>
<link href="https://fonts.googleapis.com/css2?family=Roboto:wght@400;500;700&display=swap" rel="stylesheet">
<style>
  :root {
    --brand-red: #be1e2d;
    --brand-gray: #585956;
    --card-white: #f7f6f6;
    --soft-pink: #f1d3d6;
    --page-bg: #e9e7e4;
    --white: #ffffff;
  }
  * { box-sizing: border-box; margin: 0; padding: 0; }
  html, body {
    width: 1200px; height: 960px; overflow: hidden;
    background: var(--page-bg);
    font-family: "Roboto", Arial, sans-serif;
  }
  .card {
    position: absolute;
    width: 600px; height: 342px;
    border-radius: 18px;
    overflow: hidden;
    box-shadow: 0 3px 8px rgba(0,0,0,0.18);
  }
  .card--front { left: 302px; top: 128px; background: var(--card-white); }
  .card--back { left: 300px; top: 488px; background: var(--brand-red); color: var(--white); text-align: center; }

  .hero-art {
    position: absolute; left: 250px; top: 0; width: 350px; height: 342px;
    background: radial-gradient(ellipse at 60% 45%, #ecc3c8 0%, var(--soft-pink) 55%, rgba(241,211,214,0) 80%);
  }
  .holder { position: absolute; left: 41px; top: 44px; }
  .holder__name { color: var(--brand-red); font-weight: 700; font-size: 23px; letter-spacing: 0.2px; }
  .holder__title { color: var(--brand-gray); font-weight: 500; font-size: 15px; margin-top: 2px; }
  .contacts { list-style: none; position: absolute; left: 42px; top: 102px; }
  .contacts li {
    display: flex; align-items: center; gap: 9px;
    color: var(--brand-gray); font-size: 14.5px; height: 19.2px;
  }
  .contacts svg { width: 13px; height: 13px; fill: var(--brand-red); flex: none; }
  .brand-name {
    position: absolute; left: 36px; top: 262px;
    color: var(--brand-gray); font-size: 30px; font-weight: 400; letter-spacing: -0.5px;
  }

  .company-name {
    position: absolute; left: 0; right: 0; top: 176px;
    font-weight: 500; font-size: 26px; line-height: 1.2;
  }
  .mission { position: absolute; left: 0; right: 0; top: 271px; }
  .mission__label { font-weight: 700; font-size: 19px; }
  .mission__text { font-weight: 400; font-size: 19px; margin-top: 1px; }
</style>
</head>
<body>
  <section class="card card--front">
    <div class="hero-art" role="img" aria-label="Illustration of a person sitting with a cat and a dog inside a large heart"></div>
    <div class="holder">
      <h1 class="holder__name">MARLA QUINTON</h1>
      <p class="holder__title">CEO/Founder</p>
    </div>
    <ul class="contacts">
      <li><svg viewBox="0 0 16 16"><path d="M3.5 1l3 3-1.6 2c1 2 2.6 3.6 4.6 4.6l2-1.6 3 3-2 2.5C7 14 2 9 1 3.5z"/></svg>555 214 7730</li>
      <li><svg viewBox="0 0 16 16"><path d="M4 0h8v16H4zM5.5 2v10h5V2zM7 13.2h2v1.4H7z" fill-rule="evenodd"/></svg>555 382 0496</li>
      <li><svg viewBox="0 0 16 16"><path d="M1 3h14v10H1z"/><path d="M1 3l7 6 7-6" fill="none" stroke="#f7f6f6" stroke-width="1.3"/></svg>marla@pawcarthub</li>
      <li><svg viewBox="0 0 16 16"><circle cx="8" cy="8" r="7"/><path d="M1 8h14M8 1c-3 3.5-3 10.5 0 14M8 1c3 3.5 3 10.5 0 14" fill="none" stroke="#f7f6f6" stroke-width="1.1"/></svg>www.pawcarthub</li>
      <li><svg viewBox="0 0 16 16"><rect x="1" y="1" width="14" height="14" rx="2"/></svg>Marla Quinton</li>
    </ul>
    <p class="brand-name">PawCartHub</p>
  </section>

  <section class="card card--back">
    <p class="company-name">Brindlow Veterinary Solutions</p>
    <div class="mission">
      <p class="mission__label">MISSION STATEMENT</p>
      <p class="mission__text">WE LOVE PETS!</p>
    </div>
  </section>
</body>
</html>
```